Piano-centered Instrumental Jazz Album Needs Cover Artwork

The cover has five parts, each one has obligatory features:

I. Main cover

1. Title: Velvet Keys I.
2. Artist: Marbleway Quartet
3. Design image*

* The main design motive can be something that suggests the number 4 (quartet), the sun (sunlight, sun rays), music, piano, notes, nature… Can, but doesn’t have to be one or more of these. But it should represent what the title says.
* I prefer zen-like, minimalist solutions.
* NO stock images, please! Except for unrecognizable parts of something.

II. Cover inside

1. Track list (18 songs) with durations
2. All songs written by Tibor Renvald
3. Copyright Drelbmusic 2016.
4. Design image

III. Disc

1. Artist: Marbleway Quartet
2. Title: Velvet Keys I.
3. All songs written by Tibor Renvald (round on the edge)
4. Copyright Drelbmusic 2016. (round on the edge)
5. www.drelbmusic.com (round on the edge)

IV. Cover back

1. Track list (same as cover inside)
4. www.drelbmusic.com
5. design image (optional)
6. The paper of this page is longer than the main cover, because it is to be turned up when put in the CD case, and there is the saddle with the name of the Artist and Title of the album. On both ends.

V. Under the disc

1. No words, only some design feature.

Important:
The main cover I need in RGB and also CMYK, all the others only CMYK.
I need the work file (cdr, ai or whatever you use)
I need the CMYK images prepared for printing (sizes set, and that little extra on the edges).
I need the RGB main cover cover in jpeg, 3000x3000 pixels.
That's all. :)

The most important of these all is of course the main cover RGB. Do this one first!

Here’s a sample to listen, it might inspire you:

https://files.vexlorahost.net/u/83047162/marbleway%20quartet%20sample%2020160103.mp3

If you take a closer look at my website, you can see the whole concept.

Good luck and enjoy!
Regards,
Tibor

Requirements
Must have
• Tracklist:
• 1 First, in G 05:08
• 2 Second, in Em 05:11
• 3 Third, in G 05:09
• 4 Fourth, in A 05:07
• 5 Fifth, in Bm 05:01
• 6 Sixth, in A 05:11
• 7 Seventh, in G 05:07
• 8 Eighth, in Bm 05:06
• 9 Ninth, in Gm 05:04
• 10 Tenth, in E 05:03
• 11 Eleventh, in G 05:12
• 12 Twelfth, in A 05:09
• 13 Thirteenth, in E 05:10
• 14 Fourteenth, in Am 05:14
• 15 Fifteenth, in F 05:05
• 16 Sixteenth, in Am 05:05
• 17 Seventeenth, in F 05:04
• 18 Eighteenth, in D 05:07
Should not have
• Stock images copy-pasted, additional copyright costs.

```html
<!DOCTYPE html>
<html lang="en">
<head>
<meta charset="utf-8">
<title>Marbleway Quartet – Velvet Keys I – CD Package</title>
<link rel="stylesheet" href="https://fonts.googleapis.com/css2?family=Fira+Sans+Extra+Condensed:wght@300;400;600;700&display=swap">
<style>
  :root {
    --page: #f3f3f3;
    --red-deep: #b3141c;
    --red: #d9261f;
    --orange: #ee5a1c;
    --amber: #f69a2a;
    --yellow: #fbd348;
    --cream: #fdf0c6;
    --ink-light: #ffffff;
    --ink-soft: #fde6d4;
    --disc-white: #ffffff;
    --hub: #d8d6d2;
    --hub-edge: #bdb9b4;
    --brand-red: #d31f26;
    --brand-orange: #ef5a21;
  }
  * { box-sizing: border-box; margin: 0; padding: 0; }
  html, body { width: 1200px; height: 1123px; overflow: hidden; background: var(--page); }
  body { position: relative; font-family: "Fira Sans Extra Condensed", sans-serif; }

  .panel { position: absolute; overflow: hidden; }
  .artwork { position: absolute; inset: 0; }

  /* I. Front cover */
  .front-cover { left: 112px; top: 66px; width: 456px; height: 446px; }
  .front-cover .artwork {
    background:
      radial-gradient(ellipse 55% 45% at 42% 28%, var(--cream) 0%, rgba(253,240,198,0.7) 35%, rgba(246,154,42,0) 75%),
      linear-gradient(180deg, var(--yellow) 0%, var(--amber) 35%, var(--orange) 60%, var(--red) 100%);
  }
  .cover-title { position: absolute; left: 55px; top: 352px; color: var(--ink-light); line-height: 1; font-weight: normal; }
  .cover-title .artist { font-weight: 700; font-size: 27px; letter-spacing: 0.3px; }
  .cover-title .album { font-weight: 300; font-size: 26px; margin-top: 4px; }

  /* Track lists */
  .tracklist { list-style: none; color: var(--ink-light); position: absolute; }
  .tracklist li { display: block; white-space: nowrap; overflow: visible; }
  .tracklist span { line-height: 1; }
  .tracklist .num, .tracklist .time { font-size: 0.82em; color: var(--ink-soft); }
  .tracklist .name { font-weight: 400; }
  .credits { position: absolute; color: var(--ink-light); font-weight: 300; }
  .credits p { white-space: nowrap; }
  .credits strong { font-weight: 400; font-size: 1.12em; }

  /* IV. Back tray card */
  .back-card { left: 622px; top: 68px; width: 518px; height: 438px; }
  .back-card .artwork {
    background:
      radial-gradient(ellipse 40% 25% at 20% 8%, var(--cream) 0%, rgba(253,240,198,0) 80%),
      linear-gradient(160deg, var(--amber) 0%, var(--orange) 35%, var(--red) 70%, var(--red-deep) 100%);
  }
  .back-card .tracklist { left: 28px; top: 72px; font-size: 12.5px; }
  .back-card .tracklist li { height: 15.9px; line-height: 15.9px; }
  .back-card .credits { left: 30px; top: 372px; font-size: 11px; line-height: 17px; }

  /* II. Inside cover */
  .inside-cover { left: 78px; top: 578px; width: 486px; height: 474px; }
  .inside-cover .artwork {
    background:
      radial-gradient(ellipse 40% 22% at 52% 6%, var(--cream) 0%, rgba(253,240,198,0.5) 40%, rgba(253,240,198,0) 80%),
      linear-gradient(170deg, var(--orange) 0%, var(--red) 40%, var(--orange) 65%, var(--red) 100%);
  }
  .inside-cover .tracklist { left: 36px; top: 100px; font-size: 13.5px; }
  .inside-cover .tracklist li { height: 16.8px; line-height: 16.8px; }
  .inside-cover .credits { left: 38px; top: 418px; font-size: 12px; line-height: 18px; }

  /* V. Under-disc tray + III. Disc */
  .tray { left: 590px; top: 582px; width: 548px; height: 470px; }
  .tray .artwork {
    background:
      radial-gradient(ellipse 35% 30% at 15% 15%, var(--cream) 0%, rgba(253,240,198,0) 80%),
      linear-gradient(135deg, var(--yellow) 0%, var(--amber) 30%, var(--orange) 60%, var(--red) 100%);
  }
  .disc { position: absolute; left: 58px; top: 10px; width: 448px; height: 448px; }
  .disc-edge-text { font-family: "Fira Sans Extra Condensed", sans-serif; font-size: 7.8px; fill: var(--brand-red); font-weight: 400; }
  .disc-artist { font-family: "Fira Sans Extra Condensed", sans-serif; font-weight: 700; font-size: 21px; fill: var(--brand-red); }
  .disc-album { font-family: "Fira Sans Extra Condensed", sans-serif; font-weight: 300; font-size: 21px; fill: var(--brand-orange); }
</style>
</head>
<body>

<section class="panel front-cover">
  <div class="artwork" role="img" aria-label="Low-poly sunset forest: slender dark red tree trunks against a glowing yellow, orange and red faceted sky"></div>
  <h1 class="cover-title">
    <div class="artist">MARBLEWAY QUARTET</div>
    <div class="album">Velvet Keys I</div>
  </h1>
</section>

<section class="panel back-card">
  <div class="artwork" role="img" aria-label="Low-poly forest of tall red trunks over faceted orange and red ground"></div>
  <ol class="tracklist">
    <li><span class="num">01</span> <span class="name">First, in G</span> <span class="time">05:08</span></li>
    <li><span class="num">02</span> <span class="name">Second, in Em</span> <span class="time">05:11</span></li>
    <li><span class="num">03</span> <span class="name">Third, in G</span> <span class="time">05:09</span></li>
    <li><span class="num">04</span> <span class="name">Fourth, in A</span> <span class="time">05:07</span></li>
    <li><span class="num">05</span> <span class="name">Fifth, in Bm</span> <span class="time">05:01</span></li>
    <li><span class="num">06</span> <span class="name">Sixth, in A</span> <span class="time">05:11</span></li>
    <li><span class="num">07</span> <span class="name">Seventh, in G</span> <span class="time">05:07</span></li>
    <li><span class="num">08</span> <span class="name">Eighth, in Bm</span> <span class="time">05:06</span></li>
    <li><span class="num">09</span> <span class="name">Ninth, in Gm</span> <span class="time">05:04</span></li>
    <li><span class="num">10</span> <span class="name">Tenth, in E</span> <span class="time">05:03</span></li>
    <li><span class="num">11</span> <span class="name">Eleventh, in G</span> <span class="time">05:12</span></li>
    <li><span class="num">12</span> <span class="name">Twelfth, in A</span> <span class="time">05:09</span></li>
    <li><span class="num">13</span> <span class="name">Thirteenth, in E</span> <span class="time">05:10</span></li>
    <li><span class="num">14</span> <span class="name">Fourteenth, in Am</span> <span class="time">05:14</span></li>
    <li><span class="num">15</span> <span class="name">Fifteenth, in F</span> <span class="time">05:05</span></li>
    <li><span class="num">16</span> <span class="name">Sixteenth, in Am</span> <span class="time">05:05</span></li>
    <li><span class="num">17</span> <span class="name">Seventeenth, in F</span> <span class="time">05:04</span></li>
    <li><span class="num">18</span> <span class="name">Eighteenth, in D</span> <span class="time">05:07</span></li>
  </ol>
  <div class="credits">
    <p>All songs written by <strong>Tibor Renvald</strong></p>
    <p>© 2016 Drelbmusic, All Rights Reserved</p>
    <p>www.drelbmusic.com</p>
  </div>
</section>

<section class="panel inside-cover">
  <div class="artwork" role="img" aria-label="Low-poly scene of red tree trunks with a pale sun glow in faceted red and orange"></div>
  <ol class="tracklist">
    <li><span class="num">01</span> <span class="name">First, in G</span> <span class="time">05:08</span></li>
    <li><span class="num">02</span> <span class="name">Second, in Em</span> <span class="time">05:11</span></li>
    <li><span class="num">03</span> <span class="name">Third, in G</span> <span class="time">05:09</span></li>
    <li><span class="num">04</span> <span class="name">Fourth, in A</span> <span class="time">05:07</span></li>
    <li><span class="num">05</span> <span class="name">Fifth, in Bm</span> <span class="time">05:01</span></li>
    <li><span class="num">06</span> <span class="name">Sixth, in A</span> <span class="time">05:11</span></li>
    <li><span class="num">07</span> <span class="name">Seventh, in G</span> <span class="time">05:07</span></li>
    <li><span class="num">08</span> <span class="name">Eighth, in Bm</span> <span class="time">05:06</span></li>
    <li><span class="num">09</span> <span class="name">Ninth, in Gm</span> <span class="time">05:04</span></li>
    <li><span class="num">10</span> <span class="name">Tenth, in E</span> <span class="time">05:03</span></li>
    <li><span class="num">11</span> <span class="name">Eleventh, in G</span> <span class="time">05:12</span></li>
    <li><span class="num">12</span> <span class="name">Twelfth, in A</span> <span class="time">05:09</span></li>
    <li><span class="num">13</span> <span class="name">Thirteenth, in E</span> <span class="time">05:10</span></li>
    <li><span class="num">14</span> <span class="name">Fourteenth, in Am</span> <span class="time">05:14</span></li>
    <li><span class="num">15</span> <span class="name">Fifteenth, in F</span> <span class="time">05:05</span></li>
    <li><span class="num">16</span> <span class="name">Sixteenth, in Am</span> <span class="time">05:05</span></li>
    <li><span class="num">17</span> <span class="name">Seventeenth, in F</span> <span class="time">05:04</span></li>
    <li><span class="num">18</span> <span class="name">Eighteenth, in D</span> <span class="time">05:07</span></li>
  </ol>
  <div class="credits">
    <p>All songs written by <strong>Tibor Renvald</strong></p>
    <p>© 2016 Drelbmusic, All Rights Reserved</p>
  </div>
</section>

<section class="panel tray">
  <div class="artwork" role="img" aria-label="Faceted low-poly pattern in yellow, orange and red beneath the disc"></div>
  <svg class="disc" viewBox="-224 -224 448 448" aria-label="Disc label">
    <defs>
      <radialGradient id="disc-art" cx="45%" cy="35%" r="70%">
        <stop offset="0%" stop-color="#f47a2a"/>
        <stop offset="55%" stop-color="#e2361f"/>
        <stop offset="100%" stop-color="#c81d1e"/>
      </radialGradient>
      <path id="edge-left" d="M -71.8 197.3 A 210 210 0 0 1 68.4 -198.6"/>
      <path id="edge-right" d="M 88.7 -190.3 A 210 210 0 0 1 54.4 202.8"/>
    </defs>
    <circle r="222" fill="var(--disc-white)" stroke="#e6e2dc" stroke-width="1.5"/>
    <circle r="144" fill="url(#disc-art)" role="img" aria-label="Low-poly red and orange facets on the disc face"/>
    <circle r="60" fill="var(--hub)" stroke="var(--hub-edge)" stroke-width="3"/>
    <circle r="44" fill="#e8e6e2" stroke="#cfcac4" stroke-width="1"/>
    <circle r="14" fill="var(--page)" stroke="#c9c4be" stroke-width="1"/>
    <text class="disc-edge-text"><textPath href="#edge-left">All songs written by Tibor Renvald © 2016 Drelbmusic. All rights reserved. Unauthorized duplication is a violation of applicable laws. www.drelbmusic.com</textPath></text>
    <text class="disc-edge-text"><textPath href="#edge-right">All songs written by Tibor Renvald © 2016 Drelbmusic. All rights reserved. Unauthorized duplication is a violation of applicable laws. www.drelbmusic.com</textPath></text>
    <text class="disc-artist" x="-66" y="170" textLength="168" lengthAdjust="spacingAndGlyphs">MARBLEWAY QUARTET</text>
    <text class="disc-album" x="-66" y="195">Velvet Keys I</text>
  </svg>
</section>

</body>
</html>
```